New! Cannabis Infused Chocolates - help us look yummy!

We are a well established cannabis company in Washington State, looking to launch a new line of cannabis infused chocolate squares.

Please see the uploaded inspiration pics - we are hoping to see a collage of the raw ingredients along the side of the front panel of the bag, or possibly as a background texture, but we want to capitalize on the trend of chocolate as "artwork" with the elements that are added to it (toffee or raspberries or nuts etc etc). In this case - raw ingredients illustrations/photos could be chocolate pieces, cocoa beans, leaves or flower of a cocoa plant, toffee pieces/chunks, other decorative elements.

There are a number of "required elements" for state compliance in our state, so I will upload an example of our current 'VOLTA' brand Mint Chocolate packaging so you can see how those "required elements" appear (Not for Kids icon, 21+ icon, the weight, the serving size information, 100mg THC/bag, General Use badge, Nano badge, and all the warning language is the same for this product as the Mint example bag I have uploaded). Please reference the Mint packaging for the icons and copy ONLY - For this contest, we are looking for something drawing from the inspiration pics uploaded.

We are most concerned with the visual concept - so no need to get all the placements, or all of the required elements for this initial contest, we can work together to perfect it once chosen. But in past competitions, designers have found it helpful to know for placement.

***NO CANNABIS IMAGERY PLEASE***

The products are sold in specialty dispensaries so customers are aware the products contain THC. We are more so looking for retail packaging that is trendy, modern, eye catching and enticing for a chocolate food product. The product should look premium and appetizing.

**I have also uploaded several inspiration photos. Design elements such as coco beans, crumbs, flowers, and squares of chocolates are encouraged but please feel free to get creative! We appreciate the designers efforts to put their own twist on the design.

PLEASE NOTE: This is a one bag design - each bag will contain a different flavor but for the purpose of this brief, we are focusing on Toffee Chocolate Bites.

***PLEASE NOTE: For the purpose of this brief, we are focusing on one Chocolate Toffee bag. The winner will have the opportunity to work with us on a 1-1 project to complete the other 5 products in the lineup which are - strawberry, raspberry, peanut butter chip, rice crispy and hemp heart and S'mores*****

Target Market(s)

21+ cannabis chocolate lovers in Washington state

Industry/Entity Type

Cannabis edibles

Requirements
Must have
• Delicious looking renderings of the food - chocolate, toffee, cocoa beans etc
Nice to have
• A collage of the ingredients - the ingredients as artwork - visually appealing and yummy!
Should not have
• NO CANNABIS leaves please. No need to push marijuana imagery.

```html
<!DOCTYPE html>
<html lang="en">
<head>
<meta charset="utf-8">
<title>VOLTA Toffee Chocolate Bites – Pouch Front and Back</title>
<link rel="stylesheet" href="https://fonts.googleapis.com/css2?family=Fredoka:wght@600&family=Montserrat:wght@400;600;700;800&display=swap">
<style>
  :root {
    --stage: #efe7df;
    --cocoa: #5a3324;
    --cocoa-dark: #4a2a1d;
    --kraft: #e9c7a6;
    --cream: #ece6d8;
    --toffee: #e6c2a0;
    --mint: #1fb57a;
    --ink: #f4ece4;
    --badge-yellow: #f2e600;
    --badge-red: #e23a2c;
    --hole: #e5463a;
  }
  * { box-sizing: border-box; margin: 0; padding: 0; }
  html, body { width: 1200px; height: 973px; overflow: hidden; }
  body {
    background: var(--stage);
    font-family: "Montserrat", sans-serif;
    position: relative;
  }
  .pouch {
    position: absolute;
    top: 56px;
    width: 500px;
    height: 860px;
    border-radius: 14px 14px 10px 10px;
    overflow: hidden;
    background: var(--cocoa);
    color: var(--ink);
  }
  .pouch--front { left: 60px; }
  .pouch--back { left: 640px; }
  .pouch__base {
    position: absolute; left: 0; right: 0; bottom: 0;
    background: var(--kraft);
  }
  .pouch--front .pouch__base { height: 160px; }
  .pouch--back .pouch__base { height: 130px; }
  .hang-hole {
    position: absolute; width: 18px; height: 18px; border-radius: 50%;
    background: var(--hole); top: 46px; left: 262px;
  }
  .brand-tab {
    position: absolute; left: 40px; top: 0;
    width: 172px; height: 222px;
    background: var(--cream);
    border-bottom: 12px solid var(--mint);
    display: flex; align-items: flex-end; justify-content: center;
    padding-bottom: 22px;
  }
  .brand-tab__name {
    font-weight: 600;
    font-size: 30px;
    letter-spacing: 2px;
    color: var(--cocoa-dark);
  }
  .collage { position: absolute; }
  .pouch--front .collage {
    left: 300px; top: 270px; width: 200px; height: 430px;
    background: radial-gradient(ellipse at 60% 40%, #6b3e2b 0%, #3e2418 55%, #8a5a3b 80%, #d8b48a 100%);
    border-radius: 80px 0 0 60px;
  }
  .pouch--back .collage {
    left: 250px; top: 30px; width: 230px; height: 240px;
    border-radius: 40px;
    background: radial-gradient(ellipse at 50% 45%, #6a3d29 0%, #3d2317 50%, #b98a5c 85%, rgba(90,51,36,0) 100%);
  }
  .compliance {
    position: absolute; top: 62px; right: 22px;
    display: flex; gap: 14px; align-items: flex-start;
  }
  .compliance__age { width: 64px; height: 64px; }
  .compliance__kids {
    width: 46px; height: 84px; background: #fff; border: 4px solid var(--badge-red);
  }
  .strain-tag {
    position: absolute; right: 26px; top: 200px;
    background: var(--toffee); color: var(--cocoa-dark);
    font-weight: 800; font-size: 24px;
    padding: 6px 14px; border-radius: 10px;
  }
  .title {
    position: absolute; left: 40px;
    font-family: "Fredoka", sans-serif;
    font-weight: 600;
    font-size: 118px;
    line-height: 1;
    color: var(--toffee);
    letter-spacing: 1px;
  }
  .subtitle {
    position: absolute; left: 44px;
    font-weight: 800; font-size: 27px; letter-spacing: 3px;
    color: var(--ink);
  }
  .pouch--front .title { top: 300px; }
  .pouch--front .subtitle { top: 432px; }
  .pouch--back .title { top: 300px; left: 36px; }
  .pouch--back .subtitle { top: 420px; left: 40px; }
  .spectrum {
    position: absolute; left: 44px; top: 574px;
    font-size: 15px; font-weight: 400; line-height: 1.4; letter-spacing: .5px;
  }
  .potency {
    position: absolute; left: 44px; top: 634px;
    border: 2px solid var(--toffee); border-radius: 6px;
    padding: 4px 12px; text-align: center; line-height: 1;
    color: var(--ink);
  }
  .potency__amount { font-size: 14px; font-weight: 600; display: block; }
  .potency__unit { font-size: 22px; font-weight: 800; display: block; }
  .nano {
    position: absolute; left: 44px; top: 722px; color: var(--cocoa-dark);
  }
  .nano__name { font-weight: 800; font-size: 26px; line-height: 1; }
  .nano__detail { font-weight: 800; font-size: 9px; line-height: 1.1; text-transform: uppercase; }
  .nano__speed {
    margin-top: 6px; background: var(--mint); color: #fff; display: inline-block;
    padding: 2px 8px; line-height: 1;
  }
  .nano__speed b { font-size: 16px; display: block; }
  .nano__speed small { font-size: 8px; font-weight: 700; letter-spacing: 1px; }
  .net-weight {
    position: absolute; right: 24px; top: 744px;
    font-size: 12px; font-weight: 700; color: var(--cocoa-dark);
  }
  .ingredients {
    position: absolute; left: 40px; right: 30px; top: 470px;
    font-size: 10.5px; line-height: 1.35;
  }
  .ingredients h3 { font-size: 11px; font-weight: 700; }
  .serving {
    position: absolute; left: 40px; top: 562px; width: 250px;
    font-size: 10px;
  }
  .serving h3 { font-size: 11.5px; font-weight: 800; letter-spacing: .5px; padding-bottom: 4px; border-bottom: 1.5px solid var(--ink); }
  .serving p { padding: 5px 0; border-bottom: 1.5px solid var(--ink); }
  .serving p.serving__lead { font-weight: 400; }
  .serving p:not(.serving__lead) { font-weight: 700; }
  .warning {
    position: absolute; left: 304px; top: 562px; width: 180px;
    font-size: 9.5px; font-weight: 600; line-height: 1.35;
  }
  .marks {
    position: absolute; left: 304px; top: 660px;
    display: flex; gap: 10px; align-items: flex-start;
  }
  .marks__general {
    flex: none; width: 46px; height: 46px; border-radius: 50%;
    border: 4px solid #1d1d1d; background: #fff;
  }
  .marks__contains { display: flex; gap: 6px; font-size: 8px; font-weight: 700; line-height: 1.25; width: 124px; }
  .marks__contains svg { width: 24px; height: 22px; flex: none; }
  .marks__method { font-weight: 400; display: block; margin-top: 2px; }
</style>
</head>
<body>

  <section class="pouch pouch--front">
    <div class="pouch__base"></div>
    <div class="hang-hole"></div>
    <div class="brand-tab"><span class="brand-tab__name">VOLTA</span></div>

    <div class="compliance">
      <svg class="compliance__age" viewBox="0 0 64 64" role="img" aria-label="21+ age badge">
        <polygon points="32,2 62,32 32,62 2,32" fill="var(--badge-yellow)" stroke="#fff" stroke-width="3"/>
      </svg>
      <div class="compliance__kids" role="img" aria-label="Not for kids badge"></div>
    </div>

    <div class="strain-tag">SATIVA</div>

    <div class="collage" role="img" aria-label="Collage of chocolate squares, cocoa beans, almonds, cocoa leaves and toffee chunks"></div>

    <h1 class="title">ToFFEE</h1>
    <h2 class="subtitle">CHOCOLATE BITES</h2>

    <p class="spectrum">PURE FULL SPECTRUM<br>VOLTA DISTILATE</p>

    <div class="potency">
      <span class="potency__amount">100 MG</span>
      <span class="potency__unit">THC</span>
    </div>

    <div class="nano">
      <div class="nano__name">NANO</div>
      <div class="nano__detail">Emulsified<br>Cannabinoids</div>
      <div class="nano__speed"><b>3x FASTER</b><small>BIOAVAILABILITY</small></div>
    </div>

    <p class="net-weight">Net Wt 2.2 oz. 62g</p>
  </section>

  <section class="pouch pouch--back">
    <div class="pouch__base"></div>
    <div class="hang-hole"></div>
    <div class="brand-tab"><span class="brand-tab__name">VOLTA</span></div>

    <div class="collage" role="img" aria-label="Stack of chocolate pieces with cocoa beans, nuts, leaves and toffee"></div>

    <h1 class="title">ToFFEE</h1>
    <h2 class="subtitle">CHOCOLATE BITES</h2>

    <div class="ingredients">
      <h3>INGREDIENTS :</h3>
      <p>Green mint cookie drops (sugar, palm kernel and palm oils, whey, nonfat milk, added color, sunflower lecithin, natural flavor and vanilla, dark chocolate melts (sugar, palm kernel and palm oils, cocoa (processed with potassium carbonate) nonfat milk, sunflower lecithin and vanilla). Extracted cannabis oil.</p>
    </div>

    <div class="serving">
      <h3>SUGGESTED SERVING</h3>
      <p class="serving__lead">Start with a <b><i>single</i></b> chocolate bite (<b><i>10mg</i></b> THC) and wait one hour before enjoying more</p>
      <p>10 pieces per bag (100mg THC)</p>
      <p>10mg THC per serving</p>
      <p>1 piece per serving</p>
    </div>

    <p class="warning">Warning: Maybe habit forming. Unlawful outside Washington State. It is illegal to operate a motor vehicle while under the influence of Marijuana.<br>Caution: Intoxicating effects may be delayed by 2+ hours.</p>

    <div class="marks">
      <div class="marks__general" role="img" aria-label="General use compliance badge"></div>
      <div class="marks__contains">
        <svg viewBox="0 0 26 24" aria-hidden="true">
          <polygon points="13,2 24,22 2,22" fill="none" stroke="var(--ink)" stroke-width="2"/>
          <line x1="13" y1="9" x2="13" y2="16" stroke="var(--ink)" stroke-width="2"/>
          <circle cx="13" cy="19" r="1.2" fill="var(--ink)"/>
        </svg>
        <span>THIS PRODUCT CONTAINS MARIJUANA<span class="marks__method">Hydrocarbon extraction with butane and ethanol</span></span>
      </div>
    </div>
  </section>

</body>
</html>
```